Business Card for Voltrix

Horizontal business card for voltrix, the electrical contractor.
clean and professional looking, using company branding and colours.
I also want the blue in the logo and wording to be made a more 'electric' blue and the grey 'Voltrix' to be slightly darker.

Pleas use the following contact details:

Peter Alwick
Owner

t: 01632 960581
m: 07700 900316
e: peter@voltrix-wiring.co.uk

www.voltrix-wiring.co.uk

Industry/Entity Type

Electrical

Font styles to use
Sans Serif

```html
<!DOCTYPE html>
<html lang="en">
<head>
<meta charset="UTF-8">
<title>Voltrix Business Card – Back Side</title>
<link rel="stylesheet" href="https://fonts.googleapis.com/css2?family=Arimo:wght@400;700&display=swap">
<style>
  :root {
    --page-bg: #ffffff;
    --card-blue: #02aeef;
    --card-tint: #6dcff6;
    --card-text: #ffffff;
    --label-ink: #111111;
  }
  * { margin: 0; padding: 0; box-sizing: border-box; }
  html, body {
    width: 1200px;
    height: 1000px;
    overflow: hidden;
    background: var(--page-bg);
  }
  .sheet {
    position: relative;
    width: 1200px;
    height: 1000px;
  }
  .card-back {
    position: absolute;
    left: 85px;
    top: 172px;
    width: 1021px;
    height: 567px;
    background: var(--card-blue);
    overflow: hidden;
  }
  .card-back__brand-watermark {
    position: absolute;
    right: 34px;
    top: 236px;
    font-family: "Arimo", Arial, sans-serif;
    font-weight: 700;
    font-size: 126px;
    line-height: 1;
    color: var(--card-tint);
    white-space: nowrap;
    letter-spacing: -1px;
  }
  .card-back__website {
    position: absolute;
    left: 80px;
    top: 474px;
    font-family: "Arimo", Arial, sans-serif;
    font-weight: 400;
    font-size: 24px;
    color: var(--card-text);
    letter-spacing: 0.2px;
  }
  .side-label {
    position: absolute;
    left: 0;
    width: 1244px;
    top: 797px;
    text-align: center;
    font-family: "Arimo", Arial, sans-serif;
    font-weight: 700;
    font-size: 36px;
    color: var(--label-ink);
    letter-spacing: 0.5px;
  }
</style>
</head>
<body>
  <main class="sheet">
    <section class="card-back" aria-label="Business card back side">
      <div class="card-back__brand-watermark" aria-hidden="true">Voltrix</div>
      <p class="card-back__website">www.voltrix-wiring.co.uk</p>
    </section>
    <p class="side-label">BACK SIDE</p>
  </main>
</body>
</html>
```